Heronby Mortgage Capital Business Card

We need a business card design for our mortgage servicing company. In addition to servicing the loans of homeowners, we help homeowners with purchasing their homes and any mortgage refinancing. We would like to see designs that use the colors in the logo attached below (gold-ish yellow and navy blue), and any other design you deem fit! The design should communicate a simpler life with smart mortgages provided by Heronby.

```html
<!DOCTYPE html>
<html lang="en">
<head>
<meta charset="UTF-8">
<title>Heronby Mortgage Capital – Business Card</title>
<link rel="stylesheet" href="https://fonts.googleapis.com/css2?family=Lato:wght@400;700;900&display=swap">
<style>
  :root {
    --navy: #27215a;
    --gold: #e5b12f;
    --silver: #d3d5de;
    --white: #ffffff;
    --stage: #3a3a3c;
  }
  * { margin: 0; padding: 0; box-sizing: border-box; }
  html, body {
    width: 1200px; height: 799px; overflow: hidden;
    background: var(--stage);
    font-family: "Lato", Arial, sans-serif;
  }
  .canvas {
    position: relative; width: 1200px; height: 799px;
    display: flex; flex-direction: column; align-items: center;
    justify-content: center; gap: 40px;
  }
  .card {
    position: relative; width: 600px; height: 343px;
    background: var(--navy); border-radius: 22px;
  }
  .wordmark {
    position: absolute; left: 0; right: 0;
    text-align: center; font-weight: 900; letter-spacing: 1px;
    white-space: nowrap;
  }
  .card--front .wordmark {
    top: 128px; font-size: 58px; color: var(--silver);
  }
  .card--back .wordmark {
    top: 88px; font-size: 50px; color: var(--gold);
  }
  .holder {
    position: absolute; left: 118px; top: 236px; width: 200px; text-align: right;
  }
  .holder__name {
    color: var(--gold); font-weight: 900; font-size: 22px;
    text-transform: uppercase; letter-spacing: 0.5px;
  }
  .holder__title { color: var(--white); font-size: 14px; margin-top: 2px; }
  .divider {
    position: absolute; left: 334px; top: 226px; width: 2px; height: 66px;
    background: var(--gold);
  }
  .contacts {
    position: absolute; left: 352px; top: 226px; list-style: none;
    color: var(--white); font-size: 13px; line-height: 22px;
  }
  .contacts li { display: flex; align-items: center; gap: 8px; }
  .contacts svg { width: 12px; height: 12px; flex: none; }
</style>
</head>
<body>
<main class="canvas">
  <section class="card card--front" aria-label="Card front">
    <div class="wordmark">Heronby Mortgage</div>
  </section>

  <section class="card card--back" aria-label="Card back">
    <div class="wordmark">Heronby Mortgage</div>
    <div class="holder">
      <div class="holder__name">Daniel Reyes</div>
      <div class="holder__title">Founder &amp; CEO</div>
    </div>
    <div class="divider"></div>
    <ul class="contacts">
      <li>
        <svg viewBox="0 0 24 24" fill="var(--gold)"><path d="M6.6 10.8a15.1 15.1 0 0 0 6.6 6.6l2.2-2.2c.3-.3.7-.4 1-.2 1.1.4 2.3.6 3.6.6.6 0 1 .4 1 1V20c0 .6-.4 1-1 1A17 17 0 0 1 3 4c0-.6.4-1 1-1h3.5c.6 0 1 .4 1 1 0 1.3.2 2.5.6 3.6.1.3 0 .7-.2 1z"/></svg>
        (555) 204-3817
      </li>
      <li>
        <svg viewBox="0 0 24 24" fill="var(--gold)"><path d="M2 5h20v14H2z" opacity=".0"/><path d="M2 5h20v14H2V5zm2 2v.5l8 5 8-5V7H4z"/></svg>
        info@heronbymortgage.com
      </li>
      <li>
        <svg viewBox="0 0 24 24" fill="none" stroke="var(--gold)" stroke-width="2.4"><circle cx="12" cy="12" r="9"/><path d="M3 12h18M12 3c3 3 3 15 0 18M12 3c-3 3-3 15 0 18"/></svg>
        heronbymortgage.com
      </li>
    </ul>
  </section>
</main>
</body>
</html>
```